Party planning business card design

Galas with Wren is a party planning business

Function Planning: Weddings/Themed Parties/Children's Parties

Adult and Children's Photo Booths
Party Themed boxes,
We can find the venue, entertainment. face painters.

Children's costumes and accessories - Sell / Hire

Web: www.galaswithwren.example
Facebook: Galas with Wren

Industry/Entity Type

Party Planning

Contact Information for Business Card

Galas With Wren, Rosalind Pektrew,
Creative Director

Colors
e34297
000000

Requirements
Must have
• on my logo are you able to edit the stars to pink?

```html
<!DOCTYPE html>
<html lang="en">
<head>
<meta charset="utf-8">
<title>Galas with Wren – Business Card</title>
<link rel="stylesheet" href="https://fonts.googleapis.com/css2?family=Ubuntu:wght@300;400&display=swap">
<style>
  :root {
    --brand-pink: #e34297;
    --ink: #000000;
    --paper: #ffffff;
    --backdrop: #ececec;
    --ornament-tone: #3a1a2c;
  }
  * { margin: 0; padding: 0; box-sizing: border-box; }
  html, body {
    width: 1200px;
    height: 873px;
    overflow: hidden;
    background: var(--backdrop);
  }
  .canvas {
    position: relative;
    width: 1200px;
    height: 873px;
  }
  .business-card {
    position: absolute;
    left: 150px;
    top: 162px;
    width: 900px;
    height: 549px;
    background: var(--paper);
    box-shadow: 0 6px 22px rgba(0, 0, 0, 0.18);
    overflow: hidden;
  }
  .brand-area {
    position: absolute;
    left: 0;
    top: 0;
    width: 900px;
    height: 320px;
  }
  .brand-mark {
    position: absolute;
    left: 150px;
    top: 50px;
    width: 96px;
    height: 96px;
    border-radius: 50%;
    background: var(--brand-pink);
  }
  .brand-name {
    position: absolute;
    left: 330px;
    top: 180px;
    font-family: "Ubuntu", sans-serif;
    font-weight: 300;
    font-size: 64px;
    line-height: 80px;
    letter-spacing: 1px;
    color: var(--ink);
    white-space: nowrap;
  }
  .divider-rule {
    position: absolute;
    left: 0;
    top: 320px;
    width: 900px;
    height: 6px;
    background: var(--ink);
  }
  .contact-band {
    position: absolute;
    left: 0;
    top: 326px;
    width: 900px;
    height: 223px;
    background: var(--brand-pink);
  }
  .contact-list {
    position: absolute;
    left: 170px;
    top: 24px;
    list-style: none;
    font-family: "Ubuntu", sans-serif;
    font-weight: 400;
    font-size: 26px;
    line-height: 35px;
    color: var(--ink);
    white-space: nowrap;
  }
  .band-ornament {
    position: absolute;
    bottom: 14px;
    width: 110px;
    height: 60px;
    background: var(--ornament-tone);
    opacity: 0.35;
    border-radius: 4px;
  }
  .band-ornament--left { left: 14px; }
  .band-ornament--right { right: 14px; }
</style>
</head>
<body>
  <main class="canvas">
    <article class="business-card">
      <section class="brand-area">
        <span class="brand-mark" aria-hidden="true"></span>
        <div class="brand-name">Galas with Wren</div>
      </section>
      <div class="divider-rule"></div>
      <section class="contact-band">
        <ul class="contact-list">
          <li>Rosalind Pektrew, Creative Director</li>
          <li>Phone: 0400 123 987</li>
          <li>Facebook: Galas with Wren</li>
          <li>Web: www.galaswithwren.example</li>
          <li>Email: Rosalind@galaswithwren.example</li>
        </ul>
        <div class="band-ornament band-ornament--left" role="img" aria-label="Black floral flourish ornament in the corner"></div>
        <div class="band-ornament band-ornament--right" role="img" aria-label="Black floral flourish ornament in the corner"></div>
      </section>
    </article>
  </main>
</body>
</html>
```